Halvorsen Partners Business Card

Halvorsen Partners Civil Construction
Marcus Halvorsen
CEO
727-518-6094
Marcus@HalvorsenSiteworks.example
www.HalvorsenSiteworks.example
Site Development
Utility Construction
Excavation
40876 County Lane 19
Land O' Lakes, FL 34638

Target Market(s)

Construction and government

Industry/Entity Type

Business

Contact Information for Business Card

I want an unique design that make a statement

Number of Pages Required

1 page

Font styles to use

Colors

Designer to choose colors to be used in the design.

Requirements
Must have
• unique design, feel free to modify or change the color of my logo.
Nice to have
• extra design features like spot UV, foil accents, color edges, unique paper, or any thing that would make my card pop.
• I like the feel of the image that I attached

```html
<!DOCTYPE html>
<html lang="en">
<head>
<meta charset="utf-8">
<title>Halvorsen Partners Business Card</title>
<link rel="stylesheet" href="https://fonts.googleapis.com/css2?family=Open+Sans:wght@400;600;800&display=swap">
<style>
  :root {
    --page-bg: #eeeeee;
    --card-white: #ffffff;
    --brand-blue: #2b4bb8;
    --night-blue: #2f55e0;
    --deep-blue: #1c2d86;
    --charcoal: #2c2c2e;
    --ink: #1d1d1f;
    --muted: #5a5a5e;
    --rule: #9a9a9a;
  }
  * { box-sizing: border-box; margin: 0; padding: 0; }
  html, body {
    width: 1200px; height: 1200px; overflow: hidden;
    background: var(--page-bg);
    font-family: "Open Sans", Arial, sans-serif;
  }
  .sheet {
    width: 1200px; height: 1200px;
    display: flex; flex-direction: column; align-items: center; justify-content: center;
    gap: 40px;
  }
  .card {
    width: 840px; height: 480px; position: relative; overflow: hidden;
    box-shadow: 0 6px 18px rgba(0,0,0,0.12);
  }
  .brand {
    display: flex; align-items: center; gap: 14px;
  }
  .brand-square { flex: none; border: 3px solid currentColor; }
  .brand-name {
    display: block; font-weight: 600; text-transform: uppercase;
    letter-spacing: 0.5px; line-height: 1.1; white-space: nowrap;
  }
  .brand-sub {
    display: block; font-weight: 400; text-transform: uppercase;
    letter-spacing: 3px; white-space: nowrap; margin-top: 3px;
  }

  /* Front */
  .card-front { background: var(--charcoal); }
  .card-front .scene {
    position: absolute; inset: 0;
    background:
      linear-gradient(160deg, var(--night-blue) 0%, var(--deep-blue) 38%, #26306a 50%, var(--charcoal) 62%, var(--charcoal) 100%);
  }
  .front-brand {
    position: absolute; left: 60px; top: 200px; color: #ffffff;
  }
  .front-brand .brand-square { width: 40px; height: 40px; }
  .front-brand .brand-name { font-size: 22px; }
  .front-brand .brand-sub { font-size: 10px; }
  .services {
    position: absolute; left: 250px; top: 300px;
    color: #ffffff; font-weight: 800; font-size: 34px; line-height: 1.18;
    letter-spacing: 1.5px; text-transform: uppercase; white-space: nowrap;
  }

  /* Back */
  .card-back { background: var(--card-white); color: var(--ink); }
  .back-brand {
    position: absolute; left: 300px; top: 100px; color: var(--brand-blue);
  }
  .back-brand .brand-square { width: 46px; height: 46px; }
  .back-brand .brand-name { font-size: 26px; }
  .back-brand .brand-sub { font-size: 11px; color: var(--muted); }
  .divider {
    position: absolute; left: 300px; right: 60px; top: 200px;
    height: 1px; background: var(--rule);
  }
  .contact-row {
    position: absolute; left: 130px; right: 50px; top: 245px;
    display: flex; justify-content: space-between; align-items: flex-start;
    font-size: 15px; line-height: 1.4;
  }
  .contact-row p { white-space: nowrap; }
  .person { margin-top: 70px; }
  .person .name, .phone { font-weight: 600; }
</style>
</head>
<body>
  <main class="sheet">
    <section class="card card-front">
      <div class="scene" role="img" aria-label="Dusk photo of excavator and earthmoving equipment silhouetted on a hill against a deep blue sky"></div>
      <div class="brand front-brand">
        <span class="brand-square"></span>
        <span><span class="brand-name">Halvorsen Partners</span><span class="brand-sub">Civil Construction</span></span>
      </div>
      <div class="services">
        <p>Site Development</p>
        <p>Utility Construction</p>
        <p>Excavation</p>
      </div>
    </section>

    <section class="card card-back">
      <div class="brand back-brand">
        <span class="brand-square"></span>
        <span><span class="brand-name">Halvorsen Partners</span><span class="brand-sub">Civil Construction</span></span>
      </div>
      <div class="divider"></div>
      <div class="contact-row">
        <div class="person">
          <p class="name">Marcus Halvorsen</p>
          <p class="title">CEO</p>
        </div>
        <div class="reach">
          <p class="phone">727-518-6094</p>
          <p class="email">Marcus@HalvorsenSiteworks.example</p>
        </div>
        <div class="address">
          <p>40876 County Lane 19</p>
          <p>Land O' Lakes, FL 34638</p>
        </div>
      </div>
    </section>
  </main>
</body>
</html>
```